Visitenkarten-Design für Goldankauf und Verkauf von Trauringen
Zielgruppe
Goldankauf und Verkauf von Trauringen
Aufgabenstellung
Edel, nicht zu bunt, das Design soll sich dem Kunden einprägen, ansprechend, gerne können auch Wasserzeichen verwendet werden.

```html
<!DOCTYPE html>
<html lang="de">
<head>
<meta charset="utf-8">
<title>Aurelhaus – Visitenkarten</title>
<link href="https://fonts.googleapis.com/css2?family=Cinzel:wght@400;500&family=Libre+Baskerville&display=swap" rel="stylesheet">
<style>
  :root {
    --page: #f4f4f4;
    --card: #0b0b0b;
    --card-soft: #1a1a1a;
    --gold: #d9b865;
    --gold-light: #fff59a;
    --gold-mid: #d4b35a;
    --gold-dark: #8a5a0c;
    --text: #f2f2f2;
  }
  html, body {
    margin: 0; padding: 0;
    width: 1200px; height: 1200px;
    overflow: hidden;
    background: var(--page);
  }
  .canvas { position: relative; width: 1200px; height: 1200px; }
  .card {
    position: absolute; left: 301px; width: 606px; height: 392px;
    background: radial-gradient(ellipse at 40% 40%, var(--card-soft), var(--card) 75%);
    overflow: hidden;
  }
  .card--front { top: 199px; }
  .card--back { top: 624px; }
  .gold-band {
    position: absolute; left: 0; right: 0; height: 11px;
    background: linear-gradient(90deg, var(--gold-light), var(--gold-mid) 55%, var(--gold-dark));
  }
  .gold-band--top { top: 0; }
  .gold-band--bottom { bottom: 0; }

  .brand {
    position: absolute; left: 0; right: 0; top: 150px;
    text-align: center;
  }
  .brand__name {
    display: inline-flex; align-items: center; gap: 14px;
    font-family: "Cinzel", serif; font-weight: 500;
    font-size: 50px; letter-spacing: 2px; color: var(--gold);
  }
  .brand__dot {
    width: 22px; height: 22px; border-radius: 50%; background: var(--gold);
  }
  .brand__rule {
    width: 390px; height: 1px; margin: 6px auto 8px;
    background: var(--gold);
  }
  .brand__tagline {
    font-family: "Libre Baskerville", serif; font-size: 19px;
    color: var(--text); letter-spacing: 0.5px;
  }
  .front-web {
    position: absolute; left: 0; right: 0; top: 337px;
    text-align: center;
    font-family: "Cinzel", serif; font-size: 13px; letter-spacing: 2px;
    color: var(--gold);
  }

  .watermark-circle {
    position: absolute; right: -120px; top: -40px;
    width: 300px; height: 300px; border-radius: 50%;
    background: var(--gold); opacity: 0.28;
  }
  .owner {
    position: absolute; left: 27px; top: 158px;
    font-family: "Cinzel", serif; font-size: 30px; color: var(--gold);
    letter-spacing: -0.5px; white-space: nowrap;
  }
  .contact-row {
    position: absolute; left: 27px; display: flex; align-items: center; gap: 6px;
    font-family: "Libre Baskerville", serif; color: var(--text); white-space: nowrap;
  }
  .contact-row--main { top: 199px; font-size: 15px; }
  .contact-row--small { font-size: 12.5px; gap: 5px; }
  .contact-row--addr { top: 300px; }
  .contact-row--web { top: 321px; }
  .contact-row--tel { top: 342px; }
  .icon { width: 14px; height: 14px; fill: var(--gold); flex: none; }
  .contact-row--main .icon { width: 17px; height: 17px; }
  .gap { width: 10px; }
  .sep { color: var(--gold); margin: 0 2px; }
</style>
</head>
<body>
<div class="canvas">

  <section class="card card--front">
    <div class="gold-band gold-band--top"></div>
    <div class="brand">
      <div class="brand__name"><span class="brand__dot"></span>Aurelhaus</div>
      <div class="brand__rule"></div>
      <div class="brand__tagline">Goldankauf &amp; Trauringe</div>
    </div>
    <div class="front-web">WWW.AURELHAUS-MUSTERSTADT.DE</div>
    <div class="gold-band gold-band--bottom"></div>
  </section>

  <section class="card card--back">
    <div class="watermark-circle"></div>
    <div class="owner">INH. MARA FELDHAUSEN</div>

    <div class="contact-row contact-row--main">
      <svg class="icon" viewBox="0 0 24 24"><path d="M6.6 10.8a15 15 0 0 0 6.6 6.6l2.2-2.2c.3-.3.7-.4 1-.2 1.1.4 2.3.6 3.6.6.6 0 1 .4 1 1V20c0 .6-.4 1-1 1A17 17 0 0 1 3 4c0-.6.4-1 1-1h3.5c.6 0 1 .4 1 1 0 1.3.2 2.5.6 3.6.1.3 0 .7-.2 1z"/></svg>
      <span>Mobil: 06181-5550142</span><span class="gap"></span>
      <svg class="icon" viewBox="0 0 24 24"><path d="M2 5h20v14H2z M2 5l10 8 10-8" fill="none" stroke="#d9b865" stroke-width="0"/><path d="M2 5h20v2l-10 7L2 7z"/><path d="M2 9l10 7 10-7v10H2z"/></svg>
      <span>info@aurelhaus-musterstadt.de</span>
    </div>

    <div class="contact-row contact-row--small contact-row--addr">
      <svg class="icon" viewBox="0 0 24 24"><path d="M12 2a7 7 0 0 0-7 7c0 5 7 13 7 13s7-8 7-13a7 7 0 0 0-7-7zm0 9.5A2.5 2.5 0 1 1 12 6.5a2.5 2.5 0 0 1 0 5z"/></svg>
      <span>Lindenweg 12</span><span class="sep">•</span><span>63450 Musterstadt</span>
    </div>
    <div class="contact-row contact-row--small contact-row--web">
      <svg class="icon" viewBox="0 0 24 24"><circle cx="12" cy="12" r="9" fill="none" stroke="#d9b865" stroke-width="2"/><ellipse cx="12" cy="12" rx="4" ry="9" fill="none" stroke="#d9b865" stroke-width="1.5"/><path d="M3 12h18M5 7h14M5 17h14" stroke="#d9b865" stroke-width="1.5"/></svg>
      <span>www.aurelhaus-musterstadt.de</span><span class="gap"></span>
      <svg class="icon" viewBox="0 0 24 24"><path d="M2 5h20v2l-10 7L2 7z"/><path d="M2 9l10 7 10-7v10H2z"/></svg>
      <span>info@aurelhaus-musterstadt.de</span>
    </div>
    <div class="contact-row contact-row--small contact-row--tel">
      <svg class="icon" viewBox="0 0 24 24"><path d="M6.6 10.8a15 15 0 0 0 6.6 6.6l2.2-2.2c.3-.3.7-.4 1-.2 1.1.4 2.3.6 3.6.6.6 0 1 .4 1 1V20c0 .6-.4 1-1 1A17 17 0 0 1 3 4c0-.6.4-1 1-1h3.5c.6 0 1 .4 1 1 0 1.3.2 2.5.6 3.6.1.3 0 .7-.2 1z"/></svg>
      <span>Tel.: 06181-5550142</span>
      <svg class="icon" viewBox="0 0 24 24"><rect x="2" y="8" width="4" height="13"/><path d="M8 10h14v11H8z"/><path d="M10 3h9v5h-9z"/></svg>
      <span>Fax: 06181-5550143</span>
    </div>
    <div class="gold-band gold-band--bottom"></div>
  </section>

</div>
</body>
</html>
```